Real Estate "For Sale" Sign for construction company

We need a sign that we can use to hang on a post and place on the road when we sell a property. The sign will be simple and will need to mainly feature our logo (files attached), as well as the words "For Sale", and then our phone number "(555) 617 3489". The sign will hang on a post that'll look something like the attached picture.

Target Market(s)

Home buyers

Industry/Entity Type

Real Estate

Font styles to use
Serif
Sans Serif

Colors
0054AA
0677BA
7BADD7
CADEEF
E8F1F8
0094D4
00A9DD
6FCCEA
C7EBF8
E9F6FB

Requirements
Must have
• For Sale & our phone number

```html
<!DOCTYPE html>
<html lang="en">
<head>
<meta charset="UTF-8">
<title>For Sale Sign</title>
<link rel="stylesheet" href="https://fonts.googleapis.com/css2?family=Montserrat:wght@500;600;800&display=swap">
<style>
  :root {
    --backdrop: #0054AA;
    --sign-face: #FFFFFF;
    --headline-navy: #141F4D;
    --phone-blue: #0054AA;
    --brand-blue: #0677BA;
  }
  * { margin: 0; padding: 0; box-sizing: border-box; }
  html, body {
    width: 1200px;
    height: 1200px;
    overflow: hidden;
    background: var(--backdrop);
  }
  .canvas {
    width: 1200px;
    height: 1200px;
    display: flex;
    align-items: center;
    justify-content: center;
  }
  .sign {
    width: 860px;
    height: 905px;
    background: var(--sign-face);
    display: flex;
    flex-direction: column;
    align-items: center;
    padding-top: 150px;
    font-family: "Montserrat", sans-serif;
  }
  .sign__headline {
    font-weight: 800;
    font-size: 134px;
    line-height: 1;
    letter-spacing: 1px;
    color: var(--headline-navy);
  }
  .sign__phone {
    margin-top: 40px;
    font-weight: 600;
    font-size: 91px;
    line-height: 1;
    color: var(--phone-blue);
  }
  .sign__brand {
    margin-top: 240px;
    font-weight: 500;
    font-size: 58px;
    line-height: 1;
    color: var(--brand-blue);
  }
</style>
</head>
<body>
  <main class="canvas">
    <section class="sign">
      <h1 class="sign__headline">FOR SALE</h1>
      <p class="sign__phone">(555) 617 3489</p>
      <p class="sign__brand">Cedar Ridge Homes</p>
    </section>
  </main>
</body>
</html>
```